Business card design needed

I run a Beautician studio (for 7 years now)
I offer
- Vestolin Body Sugaring
- Velumi Glow
- Nails
- Facials
- Manicure
- Foot Treatment
It might not be necessary to list all those treatments?
Maybe the link to the Website is sufficient?
I leave that up to you ...
(more info on www.BuffsAndBrowsByMarisol.com.au)
Vestolin BodySugaring is our biggest success, It replaces waxing.
I would like to incorporate the logo into the Business Card.
We had many complaints regarding our old Business Cards as the Phone Number was to small.
On the backside, we would like a "your next Appointment" section.
Looking forward to you Design, cheers ... Marisol
Buffs by Brows by Marisol
14 Merindo Cct 3912 Talvern
www.BuffsAndBrowsByMarisol.com.au
03 9418 2276

```html
<!DOCTYPE html>
<html lang="en">
<head>
<meta charset="utf-8">
<title>Vestolin Body Sugaring – Business Card</title>
<link rel="stylesheet" href="https://fonts.googleapis.com/css2?family=Arimo:wght@400&family=Tinos:wght@400;700&display=swap">
<style>
  :root {
    --stage: #3c3c3c;
    --card: #f7f7fa;
    --ornament: #c6cbf2;
    --ornament-soft: #e4e6f8;
    --rule: #b9bfe9;
    --ink: #1a1a1a;
    --ink-soft: #2b2b2b;
    --sun: #f39a2a;
  }
  * { margin: 0; padding: 0; box-sizing: border-box; }
  html, body {
    width: 1043px; height: 1200px; overflow: hidden;
    background: var(--stage);
  }
  .card {
    position: absolute; left: 30px; width: 983px;
    background: var(--card); overflow: hidden;
  }
  .card--front { top: 30px; height: 568px; }
  .card--back { top: 607px; height: 563px; }
  .ornament {
    position: absolute; inset: 0;
    background:
      radial-gradient(ellipse 62% 58% at 50% 48%, rgba(247,247,250,1) 55%, rgba(247,247,250,0) 100%),
      linear-gradient(135deg, var(--ornament) 0%, var(--ornament-soft) 45%, var(--ornament-soft) 60%, var(--ornament) 100%);
  }
  .card--back .ornament {
    opacity: .55;
    background:
      radial-gradient(ellipse 70% 60% at 50% 50%, rgba(247,247,250,1) 50%, rgba(247,247,250,0) 100%),
      linear-gradient(135deg, var(--ornament-soft) 0%, #f1f2fb 50%, var(--ornament-soft) 100%);
  }
  .brand {
    position: absolute; left: 0; right: 0; text-align: center;
    font-family: "Tinos", "Times New Roman", serif; font-weight: 400;
    color: var(--ink);
  }
  .brand__mark {
    display: block; margin: 0 auto; border-radius: 50%; background: var(--sun);
  }
  .brand__name { display: block; white-space: nowrap; }
  .brand--large { top: 110px; }
  .brand--large .brand__mark { width: 170px; height: 170px; margin-bottom: 40px; }
  .brand--large .brand__name { font-size: 56px; letter-spacing: 3px; }
  .brand--small { left: 20px; right: auto; top: 395px; width: 240px; }
  .brand--small .brand__mark { width: 72px; height: 72px; margin-bottom: 22px; }
  .brand--small .brand__name { font-size: 21px; line-height: 1.2; }

  .appointment {
    position: absolute; left: 37px; top: 40px;
    font-family: "Arimo", Arial, sans-serif; font-size: 30px; color: var(--ink-soft);
  }
  .appointment__line {
    position: absolute; left: 54px; width: 881px; height: 2px; background: var(--rule);
  }
  .services {
    position: absolute; left: 0; top: 0; width: 100%;
    font-family: "Tinos", "Times New Roman", serif; font-weight: 700;
    font-size: 32px; color: var(--ink);
  }
  .services li { position: absolute; list-style: none; white-space: nowrap; }
  .contact {
    position: absolute; right: 29px; top: 400px; text-align: right;
    font-family: "Arimo", Arial, sans-serif; font-style: normal; color: var(--ink);
  }
  .contact__studio, .contact__address { font-size: 24px; line-height: 34px; }
  .contact__phone { font-size: 40px; line-height: 48px; margin-top: 2px; }
  .contact__web { font-size: 35px; line-height: 42px; }
</style>
</head>
<body>
  <section class="card card--front">
    <div class="ornament" role="img" aria-label="Lavender floral scroll ornament framing the card edges"></div>
    <div class="brand brand--large">
      <span class="brand__mark"></span>
      <span class="brand__name">Vestolin Body Sugaring</span>
    </div>
  </section>

  <section class="card card--back">
    <div class="ornament" role="img" aria-label="Faint lavender floral scroll ornament in the background"></div>
    <p class="appointment">YOUR NEXT APPOINTMENT:</p>
    <span class="appointment__line" style="top:97px"></span>
    <span class="appointment__line" style="top:149px"></span>
    <span class="appointment__line" style="top:204px"></span>

    <ul class="services">
      <li style="left:54px; top:249px">.Vestolin Body Sugaring</li>
      <li style="left:481px; top:249px">.Nails</li>
      <li style="left:638px; top:249px">.Foot Treatment</li>
      <li style="left:188px; top:310px">.Facials</li>
      <li style="left:403px; top:310px">.Manicure</li>
      <li style="left:630px; top:310px">.Velumi Glow</li>
    </ul>

    <div class="brand brand--small">
      <span class="brand__mark"></span>
      <span class="brand__name">Vestolin Body Sugaring</span>
    </div>

    <address class="contact">
      <p class="contact__studio">Buffs by Brows by Marisol</p>
      <p class="contact__address">14 Merindo Cct 3912 Talvern</p>
      <p class="contact__phone">P: 03 9418 2276</p>
      <p class="contact__web">www.BuffsAndBrowsByMarisol.com.au</p>
    </address>
  </section>
</body>
</html>
```